Business card for apparel company. Specializing in fishing and boating performance wear. Main company name is Marlowe Teal Company, LLC brand name for apparel is WAKEFIN. See website www.WakefinReefline.com I will attach some logos to consider.

```html
<!DOCTYPE html>
<html lang="en">
<head>
<meta charset="utf-8">
<title>Wakefin Business Card</title>
<link rel="stylesheet" href="https://fonts.googleapis.com/css2?family=Lato:wght@400;700;900&display=swap">
<style>
  :root {
    --backdrop: #3a3b3e;
    --card-white: #ffffff;
    --ocean-deep: #0b3f8c;
    --ocean-mid: #1a66c2;
    --brand-blue: #1e74d6;
    --accent-orange: #f39a1e;
    --ink: #1d1d1f;
    --rule: #3bb0e8;
  }
  * { box-sizing: border-box; margin: 0; padding: 0; }
  html, body { width: 1200px; height: 851px; overflow: hidden; }
  body {
    background: var(--backdrop);
    font-family: "Lato", sans-serif;
    position: relative;
  }
  .card {
    position: absolute;
    border-radius: 22px;
    overflow: hidden;
    box-shadow: 0 18px 40px rgba(0,0,0,0.45);
  }
  /* Front */
  .card-front { left: 90px; top: 60px; width: 560px; height: 320px; }
  .card-front .photo {
    position: absolute; inset: 0;
    background:
      radial-gradient(ellipse at 25% 0%, rgba(120,200,255,0.55), transparent 55%),
      linear-gradient(180deg, var(--ocean-mid) 0%, var(--ocean-deep) 55%, #0a2d5e 100%);
  }
  .card-front .brand-name {
    position: absolute; left: 0; right: 0; top: 125px;
    text-align: center;
    color: var(--card-white);
    font-weight: 900;
    font-size: 68px;
    letter-spacing: 4px;
  }
  /* Back */
  .card-back {
    left: 480px; top: 430px; width: 630px; height: 360px;
    background: var(--card-white);
  }
  .card-back .brand-name {
    position: absolute; right: 52px; top: 44px;
    color: var(--brand-blue);
    font-weight: 900; font-size: 52px; letter-spacing: 3px;
  }
  .card-back .person { position: absolute; left: 44px; top: 150px; }
  .card-back .person-name {
    color: var(--brand-blue); font-weight: 900; font-size: 32px; letter-spacing: 0.5px;
  }
  .card-back .person-title { color: var(--ink); font-size: 19px; margin-top: 2px; }
  .card-back .divider {
    position: absolute; left: 44px; right: 44px; top: 232px;
    height: 1px; background: var(--rule);
  }
  .card-back .company { position: absolute; right: 44px; top: 248px; text-align: right; }
  .card-back .company-name { color: var(--accent-orange); font-size: 17px; }
  .card-back .company-address { color: var(--ink); font-size: 16px; line-height: 1.4; margin-top: 4px; }
  .card-back .contacts { position: absolute; left: 56px; top: 250px; list-style: none; }
  .card-back .contacts li {
    display: flex; align-items: center; gap: 10px;
    color: var(--ink); font-size: 17px; line-height: 1.65;
  }
  .card-back .contacts svg { width: 15px; height: 15px; flex: none; }
</style>
</head>
<body>
  <section class="card card-front">
    <div class="photo" role="img" aria-label="Underwater photograph of a school of fish over a coral reef in deep blue water"></div>
    <div class="brand-name">WAKEFIN</div>
  </section>

  <section class="card card-back">
    <div class="brand-name">WAKEFIN</div>

    <div class="person">
      <div class="person-name">DORIAN KELL</div>
      <div class="person-title">Founder &amp; CEO</div>
    </div>

    <div class="divider"></div>

    <ul class="contacts">
      <li>
        <svg viewBox="0 0 16 16" aria-hidden="true"><path fill="var(--brand-blue)" d="M3.6 1.5l2.2 2.6-1.3 1.6c.9 2 2.6 3.7 4.6 4.6l1.6-1.3 2.6 2.2-1.3 2.2C7 13.3 2.7 9 2.3 2.8z"/></svg>
        (555) 014-2276
      </li>
      <li>
        <svg viewBox="0 0 16 16" aria-hidden="true"><rect x="1" y="3" width="14" height="10" rx="1" fill="var(--brand-blue)"/><path d="M1.5 3.8L8 9l6.5-5.2" stroke="#fff" stroke-width="1.3" fill="none"/></svg>
        info@WakefinReefline.com
      </li>
      <li>
        <svg viewBox="0 0 16 16" aria-hidden="true"><circle cx="8" cy="8" r="6.5" fill="none" stroke="var(--brand-blue)" stroke-width="1.6"/><ellipse cx="8" cy="8" rx="2.6" ry="6.5" fill="none" stroke="var(--brand-blue)" stroke-width="1.2"/><path d="M1.5 8h13" stroke="var(--brand-blue)" stroke-width="1.2"/></svg>
        www.WakefinReefline.com
      </li>
    </ul>

    <div class="company">
      <div class="company-name">Marlowe Teal Company, LLC</div>
      <div class="company-address">P.O. Box 418<br>Harbor Vale, Florida 33910</div>
    </div>
  </section>
</body>
</html>
```